Plumix Review Divorce Law Firm Folder Insert

We are a divorce law firm.

We need a flyer just like the one that is posted. For example, that allows for our Plumix reviews to be a good deed. We do like the coloring we will provide the image that goes on the bottom right. We are open to any design. Any thoughts people have, and unique designs are welcome were very happy with this example. However, we want people to know to have some background as to what would be the best option.

Again anything but again we do want the Plumix has to be the five stars in my logo has to be on there and the portion that says these different comments included

Target Market(s)

Divorce and Custody Clients

Industry/Entity Type

Legal

Requirements
Must have
• what must remain is the Plumix logo that large, and the five stars in the front in the back. What must be included is the Plumix reviews listed below. Not all of them must be used but no less than five must be used. At least one of the five

1.) “Worth the money!”
2.) “Simply the best”
3.) “So much knowledge and experience”
4.) “When life gets challenging, you want Derek on your team!”
5.) “He made a painful divorce and custody, much easier to deal with”
6.) “Willingness to go the extra mile”
7.) “Respectful and caring”
8.) “I wouldn’t go with anyone else!”
Nice to have
• We are a divorce law firm in Harrisburg Pennsylvania. we need a Plumix review insert for our potential new clients folder. We need a hard insert flyer around 6 x 9 in height as similar possible to the one included as an attached, however we are open to any design. Since like the example so much the is a great guidepost.

We appreciate unique designs but have found one we have. To be very much to our liking. We are open to any other signs, but again. One example. Any thoughts people have, and unique designs are welcome were very happy with this example. However, we want people to know to have some background as to what would be the best option.

Attached you will find our logo, our shield by itself, the example card, and three images from which you should pick one.

one possibly to the photos can be included, but not aall three, included are three photos, only one should be used. Please pick one and use it
Should not have
• Look far off of a look that I too crazy

```html
<!DOCTYPE html>
<html lang="en">
<head>
<meta charset="utf-8">
<title>Derek R Halloway – Plumix Reviews Insert</title>
<link rel="stylesheet" href="https://fonts.googleapis.com/css2?family=Cinzel:wght@400&family=Lobster+Two:ital,wght@1,700&family=Montserrat:wght@600;700&display=swap">
<style>
  :root {
    --slate-top: #5d667b;
    --slate-mid: #545d72;
    --slate-bottom: #474f60;
    --navy: #1e2350;
    --white: #ffffff;
    --badge-ink: #3a3e46;
    --brand-ink: #e9edf4;
    --star: #f3a41f;
    --rule: rgba(255,255,255,0.35);
  }
  * { margin: 0; padding: 0; box-sizing: border-box; }
  html, body { width: 800px; height: 1200px; overflow: hidden; }
  body { background: var(--slate-mid); }

  .insert {
    position: relative;
    width: 800px;
    height: 1200px;
    overflow: hidden;
  }

  .backdrop-photo {
    position: absolute;
    inset: 0;
    background:
      radial-gradient(ellipse at 60% 35%, rgba(120,132,155,0.35), transparent 60%),
      linear-gradient(180deg, var(--slate-top) 0%, var(--slate-mid) 55%, var(--slate-bottom) 100%);
  }

  .firm-mark {
    position: absolute;
    left: 164px;
    top: 80px;
    display: flex;
    align-items: center;
    gap: 14px;
  }
  .firm-mark__square {
    width: 86px;
    height: 86px;
    background: var(--navy);
  }
  .firm-mark__name {
    font-family: "Cinzel", serif;
    font-weight: 400;
    color: var(--navy);
    line-height: 1;
  }
  .firm-mark__kicker {
    display: block;
    font-size: 14px;
    text-transform: uppercase;
    letter-spacing: 0.2px;
    margin-bottom: 3px;
  }
  .firm-mark__title {
    display: block;
    font-size: 34px;
    letter-spacing: 0.2px;
  }

  .headline {
    position: absolute;
    inset: 0;
    font-family: "Lobster Two", cursive;
    font-style: italic;
    font-weight: 700;
    color: var(--white);
    text-shadow: 3px 4px 3px rgba(20,24,36,0.75);
  }
  .headline__line {
    position: absolute;
    white-space: nowrap;
    font-size: 86px;
    line-height: 1;
    transform-origin: left bottom;
  }
  .headline__line--first {
    left: 224px;
    top: 452px;
    letter-spacing: 2px;
    transform: rotate(-10deg);
  }
  .headline__line--second {
    left: 60px;
    top: 646px;
    letter-spacing: 4px;
    transform: rotate(-14deg);
  }

  .review-badge {
    position: absolute;
    left: 492px;
    top: 704px;
    width: 244px;
    text-align: center;
    font-family: "Montserrat", sans-serif;
  }
  .review-badge__brand {
    display: block;
    font-size: 66px;
    font-weight: 700;
    color: var(--brand-ink);
    line-height: 1.05;
    letter-spacing: -1px;
  }
  .review-badge__row {
    display: flex;
    align-items: center;
    justify-content: center;
    gap: 8px;
    margin-top: 4px;
  }
  .review-badge__label {
    font-size: 22px;
    font-weight: 700;
    color: var(--badge-ink);
  }
  .review-badge__stars { display: flex; gap: 2px; }
  .review-badge__stars svg { width: 18px; height: 18px; fill: var(--star); }

  .more-reviews {
    position: absolute;
    left: 80px;
    right: 80px;
    top: 880px;
    list-style: none;
    display: grid;
    grid-template-columns: 1fr 1fr;
    gap: 26px 30px;
    font-family: "Lobster Two", cursive;
    font-style: italic;
    font-weight: 700;
    color: var(--white);
    text-shadow: 2px 3px 2px rgba(20,24,36,0.6);
    text-align: center;
  }
  .more-reviews__quote {
    font-size: 31px;
    line-height: 1.15;
    padding-top: 14px;
    border-top: 1px solid var(--rule);
  }
  .more-reviews__quote--wide { grid-column: 1 / -1; }
</style>
</head>
<body>
  <main class="insert">
    <div class="backdrop-photo" role="img" aria-label="Photo of a man in a suit silhouetted against tall office windows overlooking a city, toned slate blue"></div>

    <header class="firm-mark">
      <div class="firm-mark__square"></div>
      <h1 class="firm-mark__name">
        <span class="firm-mark__kicker">The Law Office of</span>
        <span class="firm-mark__title">DEREK R HALLOWAY</span>
      </h1>
    </header>

    <blockquote class="headline">
      <span class="headline__line headline__line--first">Willingness</span>
      <span class="headline__line headline__line--second">to go the extra mile</span>
    </blockquote>

    <div class="review-badge">
      <span class="review-badge__brand">Plumix</span>
      <div class="review-badge__row">
        <span class="review-badge__label">Reviews</span>
        <span class="review-badge__stars" aria-label="Five stars">
          <svg viewBox="0 0 24 24"><path d="M12 2l2.9 6.9 7.1.6-5.4 4.7 1.6 7-6.2-3.8-6.2 3.8 1.6-7L2 9.5l7.1-.6z"/></svg>
          <svg viewBox="0 0 24 24"><path d="M12 2l2.9 6.9 7.1.6-5.4 4.7 1.6 7-6.2-3.8-6.2 3.8 1.6-7L2 9.5l7.1-.6z"/></svg>
          <svg viewBox="0 0 24 24"><path d="M12 2l2.9 6.9 7.1.6-5.4 4.7 1.6 7-6.2-3.8-6.2 3.8 1.6-7L2 9.5l7.1-.6z"/></svg>
          <svg viewBox="0 0 24 24"><path d="M12 2l2.9 6.9 7.1.6-5.4 4.7 1.6 7-6.2-3.8-6.2 3.8 1.6-7L2 9.5l7.1-.6z"/></svg>
          <svg viewBox="0 0 24 24"><path d="M12 2l2.9 6.9 7.1.6-5.4 4.7 1.6 7-6.2-3.8-6.2 3.8 1.6-7L2 9.5l7.1-.6z"/></svg>
        </span>
      </div>
    </div>

    <ul class="more-reviews">
      <li class="more-reviews__quote">“Worth the money!”</li>
      <li class="more-reviews__quote">“Simply the best”</li>
      <li class="more-reviews__quote">“Respectful and caring”</li>
      <li class="more-reviews__quote">“So much knowledge and experience”</li>
      <li class="more-reviews__quote more-reviews__quote--wide">“I wouldn’t go with anyone else!”</li>
    </ul>
  </main>
</body>
</html>
```